Web design - Submit your captivating design
4 simple captivating pages
Web design - Submit your captivating design - Education
Creative Brief
Education
We provide affordable easily understandable innovative solutions that will enable students enjoy rapid, sustained and consistent success in the math and sciences.
Blue
Brown
top
Nav placement is up to your design. Colors should be the colors of the logo. Pages - Front page, activity page, contact us and about us page.

```html
<!DOCTYPE html>
<html lang="en">
<head>
<meta charset="utf-8">
<title>RedFerns – Dare to Succeed</title>
<link rel="stylesheet" href="https://fonts.googleapis.com/css2?family=Open+Sans:wght@400;600;700;800&display=swap">
<style>
:root{
  --brown:#a06e44;
  --brown-light:#b98654;
  --brown-dark:#2a1a10;
  --brown-footer:#33221a;
  --blue:#1c5f9c;
  --blue-dark:#0f4477;
  --orange:#f08a1c;
  --text:#333;
  --muted:#c9b9a8;
  --white:#fff;
}
*{margin:0;padding:0;box-sizing:border-box}
html,body{width:1200px;height:802px;overflow:hidden}
body{font-family:"Open Sans",Arial,sans-serif;background:var(--brown);position:relative;color:var(--text)}
.backdrop{position:absolute;left:0;top:0;width:1200px;height:612px;background:linear-gradient(90deg,var(--brown) 0%,var(--brown-light) 50%,var(--brown) 100%)}
.page{position:absolute;left:182px;top:0;width:836px;height:612px;background:var(--white);box-shadow:0 0 14px rgba(0,0,0,.35)}
.brand{position:absolute;left:18px;top:10px;display:flex;align-items:center;gap:10px}
.brand-dot{width:42px;height:42px;border-radius:50%;background:var(--orange)}
.brand-name{font-size:38px;font-weight:800;color:var(--blue);line-height:1}
.brand-tag{position:absolute;left:70px;top:56px;font-size:13px;color:var(--blue);font-weight:600}
.call{position:absolute;right:28px;top:26px;text-align:right}
.call-label{font-size:15px;font-weight:700;color:#333}
.call-number{font-size:25px;font-weight:700;color:var(--orange);display:flex;align-items:center;gap:6px;line-height:1.1}
.nav{position:absolute;left:0;top:100px;width:836px;height:40px;background:linear-gradient(var(--blue),var(--blue-dark));display:flex;border-bottom:3px solid var(--orange)}
.nav a{color:var(--white);text-decoration:none;font-size:14px;line-height:37px;padding:0 22px;border-right:1px solid rgba(255,255,255,.2)}
.nav a.active{color:var(--orange)}
.nav a:last-child{border-right:none;margin-left:auto}
.slider{position:absolute;left:6px;top:146px;width:824px;height:238px;background:linear-gradient(100deg,#d3c9b4 0%,#b8c2a6 35%,#4f6a52 70%,#3e5b46 100%);overflow:hidden}
.slider-headline{position:absolute;left:508px;top:20px;font-size:34px;font-weight:700;line-height:1.16;color:#111}
.slider-arrow{position:absolute;top:96px;width:26px;height:34px;background:rgba(255,255,255,.8);display:flex;align-items:center;justify-content:center}
.slider-arrow.prev{left:0}.slider-arrow.next{right:0}
.slider-dots{position:absolute;left:384px;top:212px;display:flex;gap:6px}
.slider-dots span{width:12px;height:12px;border-radius:50%;background:#ddd}
.slider-dots span.on{background:var(--orange)}
.features{position:absolute;left:14px;top:398px;display:flex;gap:18px}
.feature{width:193px;height:183px;background:linear-gradient(#fff,#eef2f6);border:1px solid #dde3ea;border-radius:4px;padding:12px 12px;box-shadow:0 2px 4px rgba(0,0,0,.12)}
.feature h2{font-size:14px;font-weight:700;line-height:1.1;display:flex;gap:8px;margin-bottom:8px;min-height:32px}
.feature h2 .dot{flex:none;width:22px;height:22px;border-radius:50%;background:var(--blue)}
.o{color:var(--orange)}.b{color:var(--blue)}
.feature p{font-size:11px;line-height:1.45;color:#444}
.more{display:flex;align-items:center;gap:5px;font-size:11px;color:var(--blue-dark);margin-top:22px}
.more i{width:9px;height:9px;background:var(--blue)}
.footer{position:absolute;left:0;top:612px;width:1200px;height:190px;background:var(--brown-footer);color:var(--muted)}
.col{position:absolute;top:8px;font-size:11px;line-height:1.55}
.col h3{color:var(--orange);font-size:13px;font-weight:700;margin-bottom:8px}
.links{display:flex;gap:40px}
.newsletter input{margin-top:10px;width:180px;height:22px;background:#1e130d;border:1px solid #4b3528;color:#aaa;font:11px "Open Sans",sans-serif;padding:0 6px}
.newsletter button{display:block;margin:6px 0 0 110px;background:#eee;border:none;font:11px "Open Sans",sans-serif;padding:2px 8px}
.contact dl{display:grid;grid-template-columns:46px 1fr}
.social{display:flex;gap:8px;margin-top:6px}
.social span{width:24px;height:24px;border-radius:50%;background:#6a98c9}
.copyright{position:absolute;left:0;top:160px;width:1200px;text-align:center;font-size:11px;color:var(--muted)}
</style>
</head>
<body>
<div class="backdrop"></div>
<main class="page">
  <div class="brand"><span class="brand-dot"></span><span class="brand-name">RedFerns</span></div>
  <div class="brand-tag">Dare to Succeed</div>
  <div class="call">
    <div class="call-label">Call Us Today!</div>
    <div class="call-number">
      <svg width="22" height="22" viewBox="0 0 24 24"><path d="M6.6 10.8a15 15 0 0 0 6.6 6.6l2.2-2.2c.3-.3.7-.4 1-.2 1.1.4 2.3.6 3.6.6.6 0 1 .4 1 1V20c0 .6-.4 1-1 1A17 17 0 0 1 3 4c0-.6.4-1 1-1h3.5c.6 0 1 .4 1 1 0 1.3.2 2.5.6 3.6.1.3 0 .7-.2 1z" fill="#222"/></svg>
      555-555-555
    </div>
  </div>
  <nav class="nav">
    <a class="active" href="#">Home</a><a href="#">About RedFerns</a><a href="#">RedFerns' Programs</a><a href="#">How it works</a><a href="#">Login/Signup</a><a href="#">Contact Us</a>
  </nav>
  <section class="slider">
    <div role="img" aria-label="Photo of a teacher at a chalkboard with students raising hands" style="position:absolute;inset:0"></div>
    <div class="slider-headline">Affordable.<br>Understandable.<br>Rapid Success.</div>
    <div class="slider-arrow prev"><svg width="10" height="14"><path d="M9 1L2 7l7 6" fill="none" stroke="#555" stroke-width="2"/></svg></div>
    <div class="slider-arrow next"><svg width="10" height="14"><path d="M1 1l7 6-7 6" fill="none" stroke="#555" stroke-width="2"/></svg></div>
    <div class="slider-dots"><span class="on"></span><span></span><span></span><span></span></div>
  </section>
  <section class="features">
    <article class="feature"><h2><span class="dot"></span><span><span class="o">Evening and</span><br><span class="b">Summer classes</span></span></h2><p>Lorem ipsum dolor sit amet, consectetur adipisicing elit, sed do eiusmod tempor incid-idunt ut labore et dolore magna aliqua.</p><div class="more"><i></i>Read more</div></article>
    <article class="feature"><h2><span class="dot"></span><span><span class="o">RedFerns</span> <span class="b">Tutoring</span></span></h2><p>Lorem ipsum dolor sit amet, consectetur adipisicing elit, sed do eiusmod tempor incid-idunt ut labore et dolore magna aliqua.</p><div class="more"><i></i>Read more</div></article>
    <article class="feature"><h2><span class="dot"></span><span><span class="o">Online</span> <span class="b">Notes</span></span></h2><p>Lorem ipsum dolor sit amet, consectetur adipisicing elit, sed do eiusmod tempor incid-idunt ut labore et dolore magna aliqua.</p><div class="more"><i></i>Read more</div></article>
    <article class="feature"><h2><span class="dot"></span><span><span class="o">Powerful</span> <span class="b">Billboard</span></span></h2><p>Lorem ipsum dolor sit amet, consectetur adipisicing elit, sed do eiusmod tempor incid-idunt ut labore et dolore magna aliqua.</p><div class="more"><i></i>Read more</div></article>
  </section>
</main>
<footer class="footer">
  <div class="col" style="left:186px"><h3>Navigation</h3>
    <div class="links"><div>Home<br>About RedFerns<br>RedFerns' Programs<br>How it works<br>Login/Signup</div><div>Sitemap<br>Privacy Policy<br>Contact Us</div></div></div>
  <div class="col newsletter" style="left:438px;width:200px"><h3>Subscribe Newsletter</h3>
    Join our newsletter to your latest<br>News &amp; Offers
    <input type="text" value="Enter email address"><button>Subscribe</button></div>
  <div class="col contact" style="left:686px"><h3>Contact Us</h3>
    Address line 1, address line 2<br>City, State, Country.<br><br>
    <dl><dt>Phone</dt><dd>: 555-555-555</dd><dt>Email</dt><dd>: redferns@redferns.com</dd></dl></div>
  <div class="col" style="left:918px"><h3>Follow Us</h3><div class="social"><span></span><span></span><span></span></div></div>
  <div class="copyright">Copyright © 2012, RedFerns. All rights reserved.</div>
</footer>
</body>
</html>
```